2 Redfern Pike Auto Care Banners

Looking to have two pull up banners designed - each 33.5 x 80

First banner- Scheduled Maintenance, Diagnostics, Inspections
Voted Top Pick Marbury 3 years in a row!

Second banner- Brakes, Tires, General Auto Service
Include the 3 TPM logos
2019, 2018, 2017

```html
<!DOCTYPE html>
<html lang="en">
<head>
<meta charset="utf-8">
<title>Redfern Pike Auto Care – Pull Up Banners</title>
<link href="https://fonts.googleapis.com/css2?family=Barlow+Condensed:wght@500;600&display=swap" rel="stylesheet">
<style>
  :root{
    --backdrop:#a4a4a4;
    --navy:#1c2444;
    --navy-deep:#121831;
    --ink:#07080d;
    --gold:#d3c25a;
    --gold-dark:#a8942c;
    --paper:#ffffff;
  }
  html,body{margin:0;padding:0;overflow:hidden;}
  body{width:1200px;height:2229px;background:var(--backdrop);position:relative;}
  .banner{position:absolute;top:470px;width:540px;height:1287px;display:block;}
  .banner--maintenance{left:40px;}
  .banner--service{left:620px;}
  .brand-name,.service-label,.award-text,.contact-text,.callout-text{
    font-family:"Barlow Condensed",sans-serif;
  }
  .brand-name{fill:var(--gold);font-weight:600;}
  .service-label{fill:var(--gold);font-weight:600;font-size:39px;}
  .award-text{fill:var(--navy);font-weight:600;}
  .contact-text{fill:var(--paper);font-weight:600;}
  .callout-text{fill:var(--paper);font-weight:500;}
  .icon-ring{fill:none;stroke:var(--gold);stroke-width:2.5;}
  .icon-line{fill:none;stroke:var(--gold);stroke-width:3;stroke-linecap:round;stroke-linejoin:round;}
  .icon-fill{fill:var(--gold);}
  .award-placeholder{fill:var(--paper);}
</style>
</head>
<body>

<!-- Banner one: maintenance services -->
<svg class="banner banner--maintenance" viewBox="0 0 392 934" xmlns="http://www.w3.org/2000/svg">
  <defs>
    <linearGradient id="panelFadeA" x1="0" y1="0" x2="0" y2="1">
      <stop offset="0" stop-color="#1f2747"/>
      <stop offset="0.72" stop-color="#1a2140"/>
      <stop offset="1" stop-color="#05060a"/>
    </linearGradient>
    <linearGradient id="photoShopA" x1="0" y1="0" x2="0" y2="1">
      <stop offset="0" stop-color="#3e4552"/>
      <stop offset="0.5" stop-color="#7d838c"/>
      <stop offset="1" stop-color="#1f2747"/>
    </linearGradient>
    <linearGradient id="goldBandA" x1="0" y1="0" x2="1" y2="0">
      <stop offset="0" stop-color="#b9a63d"/>
      <stop offset="0.5" stop-color="#e6d77a"/>
      <stop offset="1" stop-color="#c4b24a"/>
    </linearGradient>
  </defs>

  <rect class="panel-base" width="392" height="934" fill="url(#panelFadeA)"/>

  <g role="img" aria-label="Photo: mechanic working under a raised car in a workshop">
    <path d="M0 215 C120 170 280 175 392 235 L392 450 L0 450 Z" fill="url(#photoShopA)"/>
  </g>

  <path class="header-white" d="M0 0 H392 V215 C280 150 120 145 0 195 Z" fill="var(--paper)"/>
  <path class="header-swoosh" d="M0 195 C120 145 280 150 392 215 L392 235 C280 175 120 170 0 215 Z" fill="url(#goldBandA)"/>

  <g class="brand">
    <text class="brand-name" x="196" y="88" font-size="48" text-anchor="middle">Redfern Pike</text>
    <text class="brand-name" x="196" y="128" font-size="26" text-anchor="middle" letter-spacing="5">AUTO CARE</text>
  </g>

  <g class="service-list">
    <g class="service">
      <circle class="icon-ring" cx="66" cy="450" r="27"/>
      <path class="icon-line" d="M54 438 L78 462 M78 438 L54 462 M50 442 l8 -8 M74 458 l8 8"/>
      <text class="service-label" x="118" y="445">Scheduled</text>
      <text class="service-label" x="118" y="484">Maintenance</text>
    </g>
    <g class="service">
      <circle class="icon-ring" cx="66" cy="528" r="27"/>
      <circle class="icon-line" cx="70" cy="523" r="9"/>
      <path class="icon-line" d="M63 531 L53 541"/>
      <text class="service-label" x="120" y="545">Diagnostics</text>
    </g>
    <g class="service">
      <circle class="icon-ring" cx="66" cy="606" r="27"/>
      <circle cx="66" cy="606" r="11" fill="none" stroke="var(--gold)" stroke-width="6" stroke-dasharray="4 3"/>
      <circle class="icon-fill" cx="66" cy="606" r="8"/>
      <circle cx="66" cy="606" r="4" fill="var(--navy)"/>
      <text class="service-label" x="120" y="619">Inspections</text>
    </g>
  </g>

  <rect class="award-band" x="0" y="672" width="392" height="88" fill="url(#goldBandA)"/>

  <g class="award-callout">
    <circle cx="115" cy="716" r="68" fill="var(--navy-deep)" stroke="var(--gold-dark)" stroke-width="4"/>
    <text class="callout-text" x="115" y="710" font-size="18" text-anchor="middle">Voted Top Pick</text>
    <text class="callout-text" x="115" y="738" font-size="27" text-anchor="middle">Marbury</text>
  </g>

  <g class="award-copy">
    <text class="award-text" x="204" y="722" font-size="45">3 YEARS</text>
    <text class="award-text" x="206" y="757" font-size="31">IN A ROW!</text>
  </g>

  <g class="contact">
    <circle cx="46" cy="883" r="12" fill="none" stroke="var(--paper)" stroke-width="3"/>
    <path d="M34 883 H58 M46 871 C38 879 38 887 46 895 M46 871 C54 879 54 887 46 895" fill="none" stroke="var(--paper)" stroke-width="2.5"/>
    <text class="contact-text" x="78" y="899" font-size="39">redfernpikeauto.com</text>
  </g>
</svg>

<!-- Banner two: general service -->
<svg class="banner banner--service" viewBox="0 0 392 934" xmlns="http://www.w3.org/2000/svg">
  <defs>
    <linearGradient id="panelFadeB" x1="0" y1="0" x2="0" y2="1">
      <stop offset="0" stop-color="#1f2747"/>
      <stop offset="0.72" stop-color="#1a2140"/>
      <stop offset="1" stop-color="#05060a"/>
    </linearGradient>
    <linearGradient id="photoShopB" x1="0" y1="0" x2="0" y2="1">
      <stop offset="0" stop-color="#4c5a72"/>
      <stop offset="0.55" stop-color="#2c3a5e"/>
      <stop offset="1" stop-color="#1f2747"/>
    </linearGradient>
    <linearGradient id="goldBandB" x1="0" y1="0" x2="1" y2="0">
      <stop offset="0" stop-color="#b9a63d"/>
      <stop offset="0.5" stop-color="#e6d77a"/>
      <stop offset="1" stop-color="#c4b24a"/>
    </linearGradient>
  </defs>

  <rect class="panel-base" width="392" height="934" fill="url(#panelFadeB)"/>

  <g role="img" aria-label="Photo: smiling mechanic with arms crossed in front of an open car engine">
    <path d="M0 200 C120 240 280 240 392 200 L392 420 L0 420 Z" fill="url(#photoShopB)"/>
  </g>

  <path class="header-white" d="M0 0 H392 V175 C280 225 120 225 0 180 Z" fill="var(--paper)"/>
  <path class="header-swoosh" d="M0 180 C120 225 280 225 392 175 L392 205 C280 245 120 245 0 200 Z" fill="url(#goldBandB)"/>

  <g class="brand">
    <text class="brand-name" x="196" y="100" font-size="48" text-anchor="middle">Redfern Pike</text>
    <text class="brand-name" x="196" y="140" font-size="26" text-anchor="middle" letter-spacing="5">AUTO CARE</text>
  </g>

  <g class="service-list">
    <g class="service">
      <circle class="icon-ring" cx="72" cy="450" r="27"/>
      <path class="icon-line" d="M58 458 V450 L63 440 H81 L86 450 V458 Z M58 458 v4 M86 458 v4"/>
      <circle class="icon-fill" cx="64" cy="452" r="2"/><circle class="icon-fill" cx="80" cy="452" r="2"/>
      <text class="service-label" x="138" y="445">General</text>
      <text class="service-label" x="138" y="484">Auto Service</text>
    </g>
    <g class="service">
      <circle class="icon-ring" cx="72" cy="528" r="27"/>
      <circle class="icon-line" cx="72" cy="528" r="14"/>
      <circle class="icon-line" cx="72" cy="528" r="5"/>
      <path class="icon-line" d="M58 516 A18 18 0 0 1 72 508" stroke-width="5"/>
      <text class="service-label" x="136" y="545">Brakes</text>
    </g>
    <g class="service">
      <circle class="icon-ring" cx="72" cy="606" r="27"/>
      <circle class="icon-line" cx="72" cy="606" r="17"/>
      <circle class="icon-line" cx="72" cy="606" r="10"/>
      <path class="icon-line" d="M72 596 V616 M62 606 H82 M65 599 L79 613 M79 599 L65 613" stroke-width="2"/>
      <text class="service-label" x="136" y="619">Tires</text>
    </g>
  </g>

  <g class="award-badges" role="img" aria-label="Three award badges: 2019, 2018, 2017">
    <rect class="award-placeholder" x="16" y="685" width="111" height="66"/>
    <rect class="award-placeholder" x="140" y="685" width="111" height="66"/>
    <rect class="award-placeholder" x="265" y="685" width="111" height="66"/>
  </g>

  <g class="contact">
    <circle cx="55" cy="815" r="11" fill="none" stroke="var(--paper)" stroke-width="3"/>
    <path d="M44 815 H66 M55 804 C48 811 48 819 55 826 M55 804 C62 811 62 819 55 826" fill="none" stroke="var(--paper)" stroke-width="2.5"/>
    <text class="contact-text" x="88" y="830" font-size="37">redfernpikeauto.com</text>
    <path d="M47 862 C45 872 52 880 62 882 L65 876 L59 872 L56 875 C53 873 51 870 50 867 L53 864 L50 858 Z" fill="var(--paper)"/>
    <text class="contact-text" x="88" y="885" font-size="40">555-014-2290</text>
  </g>
</svg>

</body>
</html>
```